Sheep ranch business card design

We need a business card design for our farm. We do all things sheep. We run Babydoll southdown sheep and use their fiber and meat. In the spring the lambs are sold. We shear them for their wool to make dryer balls, roving, and yarn which we sell. We also lease the sheep out to organic vineyards in the winter time to help them convert their weeds and cover crops to manure so they don't have to use tractors and tillers to mow and compact soil. Copperfield Ranch also breeds Kangals which are livestock guard dogs that live with and protect the sheep. We also run a small herd of jersey cows, chickens, and bees but the sheep enterprise is the focal point. I would like to see the design use more earth tones and natural colors and have the feel of a modern and hip farm. I would also like our attached copperfield ranch image to be used. The font family is dalle for our logo. That font can be used or something to compliment it. The attached pictures can be used as well but they are not necessary. One copperfield ranch upload is in psd and one is in jpeg. Thank You and we look forward to seeing your work.
Updates

So many great designs. Not looking for anything "western." Font, design, or otherwise.

Industry/Entity Type

Livestock

Contact Information for Business Card

Copperfield Ranch
Tessa Pollard
www.copperfieldranch.example
copperfieldranch@mailbox.example
phone: 555 210-7389

```html
<!DOCTYPE html>
<html lang="en">
<head>
<meta charset="utf-8">
<title>Copperfield Ranch – Business Card</title>
<link rel="stylesheet" href="https://fonts.googleapis.com/css2?family=Raleway:wght@400;500&display=swap">
<style>
  :root {
    --backdrop: #ecebe7;
    --card-green: #3e5b2b;
    --card-edge: #2f4720;
    --logo-yellow: #dcc21c;
    --contact-white: #f1f1ea;
  }
  * { margin: 0; padding: 0; box-sizing: border-box; }
  html, body {
    width: 1200px;
    height: 900px;
    overflow: hidden;
    background: var(--backdrop);
  }
  .canvas {
    width: 1200px;
    height: 900px;
    display: flex;
    align-items: center;
    justify-content: center;
  }
  .business-card {
    width: 840px;
    height: 480px;
    background: var(--card-green);
    box-shadow: 0 0 0 1px var(--card-edge), 0 12px 30px rgba(0,0,0,0.18);
    display: flex;
    flex-direction: column;
    align-items: center;
    font-family: "Raleway", sans-serif;
  }
  .brand {
    margin-top: 150px;
    display: flex;
    align-items: center;
    gap: 22px;
  }
  .brand-dot {
    width: 46px;
    height: 46px;
    border-radius: 50%;
    background: var(--logo-yellow);
  }
  .brand-name {
    color: var(--logo-yellow);
    font-weight: 500;
    font-size: 50px;
    letter-spacing: 0.12em;
    text-transform: uppercase;
    line-height: 1;
  }
  .contact {
    margin-top: 96px;
    text-align: center;
    color: var(--contact-white);
    font-weight: 500;
    font-size: 25px;
    line-height: 1.35;
  }
</style>
</head>
<body>
  <main class="canvas">
    <section class="business-card">
      <div class="brand">
        <span class="brand-dot"></span>
        <h1 class="brand-name">Copperfield Ranch</h1>
      </div>
      <div class="contact">
        <p class="contact-line">Tessa Pollard | phone: 555 210-7389</p>
        <p class="contact-line">copperfieldranch@mailbox.example | www.copperfieldranch.example</p>
      </div>
    </section>
  </main>
</body>
</html>
```